Creative Real Estate Listing Mailer

I would like a creative double sided Real Estate listing flier/mailer to send out enticing people to list their house for sale with me. An example in my head, but feel free to be creative,.. would be one side with a Weiner dog with a sack of money on its back saying something like " its time to cash in" and the other side having some kind of southwest backdrop ( I live in Arizona) or luxury home, with my photo and my contact info saying something like list your house with me, or see what your home is worth etc.

Target Market(s)

People interested in selling their homes

Industry/Entity Type

Real Estate Agent

Contact Information for Business Card

Similar to the flyer, but simpler

Requirements
Must have
• My name: Milo Trask
My Email: milotrask@brevlo.com
My Phone# (480) 555 0147
Website www.Milotrask.com

```html
<!DOCTYPE html>
<html lang="en">
<head>
<meta charset="utf-8">
<title>Desert Crest Properties – Seller Mailer</title>
<link rel="stylesheet" href="https://fonts.googleapis.com/css2?family=Montserrat:wght@400;600;800;900&family=Staatliches&display=swap">
<style>
  :root{
    --navy:#1b1d3f;
    --blue:#2a8fd8;
    --blue-deep:#1f5fb8;
    --orange:#e8962b;
    --ink:#3a3a44;
    --white:#ffffff;
    --canvas:#ececec;
  }
  *{margin:0;padding:0;box-sizing:border-box}
  html,body{width:906px;height:1200px;overflow:hidden}
  body{background:var(--canvas);position:relative;font-family:"Montserrat",sans-serif}
  .slot{position:absolute;top:304px;width:420px;height:591px;box-shadow:0 2px 6px rgba(0,0,0,.18)}
  .slot--front{left:23px}
  .slot--back{left:463px}
  .sheet{position:absolute;top:0;left:0;width:618px;height:870px;transform:scale(.6796);transform-origin:0 0;background:var(--white);overflow:hidden}
  .sheet svg.art{position:absolute;inset:0}
  .t{position:absolute;white-space:nowrap}

  /* brand lockup */
  .brand{position:absolute;display:flex;align-items:center;gap:9px;color:var(--navy);font-weight:600;font-size:17px;letter-spacing:1px;white-space:nowrap}
  .brand__mark{width:26px;height:26px;background:var(--orange);flex:none}

  /* front */
  .front .brand{left:126px;top:56px}
  .headline-kicker{left:35px;top:346px;font-weight:800;font-size:49px;color:var(--orange)}
  .headline-main{left:35px;top:392px;font-weight:900;font-size:70px;color:var(--navy);letter-spacing:-1px}
  .headline-grunge{left:36px;top:466px;font-family:"Staatliches",sans-serif;font-size:56px;line-height:57px;color:var(--navy);letter-spacing:3px}
  .rule{position:absolute;left:35px;top:642px;width:290px;height:1px;background:#b9b9c4}
  .pitch{left:35px;top:658px;font-size:12.5px;line-height:17px;letter-spacing:2.4px;color:var(--ink)}
  .front .phone{left:202px;top:740px;font-weight:800;font-size:20px;color:var(--orange);display:flex;align-items:center;gap:6px}
  .offices{left:0;top:790px;width:618px;text-align:center;color:var(--white);font-size:9px;line-height:9.5px;letter-spacing:1px;font-weight:600}
  .offices .sub{font-weight:400;opacity:.7}

  /* back */
  .back .phone{left:40px;top:82px;font-weight:800;font-size:31px;color:var(--white);display:flex;align-items:center;gap:6px;letter-spacing:1px}
  .call-me{left:38px;top:134px;font-size:25px;letter-spacing:6px;color:var(--white);font-weight:400}
  .agent-name{left:34px;top:176px;font-weight:900;font-size:58px;line-height:54px;color:var(--white);letter-spacing:2px}
  .offer{left:34px;top:298px;font-weight:900;font-size:45px;line-height:48.5px;color:var(--white)}
  .contact{left:0;top:646px;width:618px;text-align:center;font-size:15px;line-height:21px;letter-spacing:2.5px;color:var(--ink)}
  .divider{position:absolute;left:0;top:754px;width:618px;height:1px;background:#cfcfd6}
  .badge{position:absolute;background:var(--navy)}
  .badge--housing{left:48px;top:768px;width:64px;height:68px}
  .badge--listing{left:140px;top:776px;width:124px;height:56px;background:none;border:3px solid var(--navy)}
  .back .brand{left:296px;top:790px;font-size:17px}
  .phone-icon{width:26px;height:26px;flex:none}
</style>
</head>
<body>

<section class="slot slot--front">
  <div class="sheet front">
    <svg class="art" viewBox="0 0 618 870" width="618" height="870">
      <defs>
        <linearGradient id="photoTone" x1="1" y1="0" x2="0" y2="1">
          <stop offset="0" stop-color="#c9b28f"/>
          <stop offset=".3" stop-color="#b98a74"/>
          <stop offset=".55" stop-color="#d8dde4"/>
          <stop offset="1" stop-color="#eef3f8"/>
        </linearGradient>
        <radialGradient id="photoFade" cx="420" cy="200" r="330" gradientUnits="userSpaceOnUse">
          <stop offset="0" stop-color="#fff"/>
          <stop offset=".6" stop-color="#fff" stop-opacity=".9"/>
          <stop offset="1" stop-color="#fff" stop-opacity="0"/>
        </radialGradient>
        <mask id="photoMask"><rect width="618" height="870" fill="url(#photoFade)"/></mask>
        <linearGradient id="swoosh" x1="0" y1="0" x2="1" y2="1">
          <stop offset="0" stop-color="#3a6fd6"/>
          <stop offset="1" stop-color="#2a8fd8"/>
        </linearGradient>
      </defs>
      <rect x="90" y="0" width="528" height="560" fill="url(#photoTone)" mask="url(#photoMask)" role="img" aria-label="Model house with a sack of money and keys resting on blueprints"/>
      <g fill="none" stroke="#d5e3f2" stroke-width="1.5">
        <circle cx="620" cy="620" r="80"/><circle cx="620" cy="620" r="110"/>
        <circle cx="620" cy="620" r="140"/><circle cx="620" cy="620" r="170"/>
      </g>
      <path d="M0,0 L120,0 C60,110 120,230 210,300 C120,280 40,240 0,200 Z" fill="var(--navy)"/>
      <path d="M0,0 L135,0 C95,110 150,200 275,250 L190,300 C110,240 40,180 0,130 Z" fill="url(#swoosh)"/>
      <path d="M125,0 L618,0 L618,20 C560,160 440,230 330,228 C210,226 120,140 125,0 Z" fill="#fff"/>
      <path d="M0,755 C250,805 470,770 618,665 L618,870 L0,870 Z" fill="var(--navy)"/>
    </svg>

    <div class="brand"><span class="brand__mark"></span>DESERT CREST PROPERTIES</div>
    <div class="t headline-kicker">SELLING YOUR</div>
    <div class="t headline-main">PROPERTY?</div>
    <div class="t headline-grunge">LET US MAKE YOU<br>A WHOLE LOAD OF<br>MONEY!</div>
    <div class="rule"></div>
    <p class="t pitch">IF YOU HAVE A HOUSE OR PROPERTY YOU ARE SELLING<br>OR THINKING OF SELLING IN ARIZONA, THIS IS IT!<br>DO NOT HESITATE TO GET IN TOUCH FOR THE BEST<br>DEAL POSSIBLE!</p>
    <div class="t phone">
      <svg class="phone-icon" viewBox="0 0 26 26" aria-hidden="true"><circle cx="13" cy="13" r="12" fill="var(--blue-deep)"/><path d="M9 7c1 0 2 2 2 3s-1 1-1 2 3 4 4 4 1-1 2-1 3 1 3 2-1 2-2 2C11 19 7 15 7 9c0-1 1-2 2-2z" fill="#fff"/></svg>
      (480) 555 0147
    </div>
    <div class="t offices">
      1180 W. Mesquite Ln., Suite 40 | Tempe, AZ 85281<br>
      <span class="sub">Phone 480-555-0192 | Fax 480-555-0193</span><br>
      2215 E. Saguaro Rd. | Payson, AZ 85541<br>
      <span class="sub">Phone 928-555-0164 | Fax 928-555-0165</span><br>
      730 N. Ocotillo Dr. Suite 8 | Gilbert, AZ 85233<br>
      <span class="sub">Phone 480-555-0178</span>
    </div>
  </div>
</section>

<section class="slot slot--back">
  <div class="sheet back">
    <svg class="art" viewBox="0 0 618 870" width="618" height="870">
      <defs>
        <clipPath id="panel"><path d="M0,120 Q0,0 120,0 L618,0 L618,615 L0,615 Z"/></clipPath>
        <linearGradient id="portraitTone" x1="0" y1="0" x2="1" y2="1">
          <stop offset="0" stop-color="#d9dcd6"/>
          <stop offset=".5" stop-color="#8d8f94"/>
          <stop offset="1" stop-color="#26305a"/>
        </linearGradient>
        <linearGradient id="ringTone" x1="0" y1="0" x2="1" y2="1">
          <stop offset="0" stop-color="#4fb0ee"/>
          <stop offset="1" stop-color="#1f5fb8"/>
        </linearGradient>
      </defs>
      <g clip-path="url(#panel)">
        <rect width="618" height="615" fill="var(--navy)"/>
        <circle cx="420" cy="300" r="300" fill="url(#ringTone)"/>
        <circle cx="420" cy="300" r="252" fill="url(#portraitTone)" role="img" aria-label="Portrait of the agent in a suit in front of a modern home"/>
        <circle cx="420" cy="300" r="236" fill="none" stroke="var(--navy)" stroke-width="9"/>
        <path d="M0,560 L0,615 L520,615 C430,610 360,560 330,520 Z" fill="var(--navy)"/>
      </g>
    </svg>

    <div class="t phone">
      <svg class="phone-icon" viewBox="0 0 26 26" aria-hidden="true" style="width:32px;height:32px"><circle cx="13" cy="13" r="12" fill="var(--blue)"/><path d="M9 7c1 0 2 2 2 3s-1 1-1 2 3 4 4 4 1-1 2-1 3 1 3 2-1 2-2 2C11 19 7 15 7 9c0-1 1-2 2-2z" fill="#fff"/></svg>
      (480) 555 0147
    </div>
    <div class="t call-me">CALL ME</div>
    <div class="t agent-name">MILO<br>TRASK</div>
    <div class="t offer">LET US<br>FIND OUT<br>HOW MUCH<br>YOUR<br>PROPERTY<br>IS WORTH</div>

    <div class="t contact">Milo Trask<br>milotrask@brevlo.com<br>(480) 555 0147<br>www.Milotrask.com</div>
    <div class="divider"></div>
    <div class="badge badge--housing"></div>
    <div class="badge badge--listing"></div>
    <div class="brand"><span class="brand__mark"></span>DESERT CREST PROPERTIES</div>
  </div>
</section>

</body>
</html>
```